Land Buying Company Needs Letterhead for Direct Mail Marketing to Land Owners

We are looking for a professional letterhead that we will be including in our direct mail marketing. We will be sending this to land owners who may be interested in selling or purchasing land.

The letterhead needs to be editable. Headers and footers would look nice, but we are open. We would want it to include our address, website, phone, and email info. For right now the address to use for design purposes would the following:

Address: 415 Bramwell Avenue #600
Dallas, TX 75219
Website - www.quillridgeacres.example
Email - info@quillridgeacres.example
Phone - 866-402-ACRE

I have attached our logo zip file that we just had done on Pixel Guild. Let me know what questions you have, and thank you.

```html
<!DOCTYPE html>
<html lang="en">
<head>
<meta charset="utf-8">
<title>Quillridge Acres Letterhead</title>
<link href="https://fonts.googleapis.com/css2?family=Arimo:wght@400;700&family=Montserrat:wght@600&display=swap" rel="stylesheet">
<style>
  :root {
    --backdrop: #eef2e6;
    --paper: #ffffff;
    --brand-green: #4a5d23;
    --brand-light: #ffffff;
    --ink: #1f1f1f;
    --watermark: #efefef;
    --signature: #d9d9d9;
  }
  * { margin: 0; padding: 0; box-sizing: border-box; }
  html, body {
    width: 1000px;
    height: 1200px;
    overflow: hidden;
    background: var(--backdrop);
  }
  .letterhead {
    position: absolute;
    left: 140px;
    top: 94px;
    width: 720px;
    height: 1012px;
    background: var(--paper);
    overflow: hidden;
    font-family: "Arimo", Arial, sans-serif;
    color: var(--ink);
  }
  .watermark-circle {
    position: absolute;
    left: 50px;
    top: 636px;
    width: 390px;
    height: 390px;
    border-radius: 50%;
    background: var(--watermark);
  }
  .header-band {
    position: relative;
    height: 150px;
    background: var(--brand-green);
    display: flex;
    justify-content: space-between;
    align-items: center;
    padding: 0 30px 0 48px;
  }
  .brand {
    display: flex;
    align-items: center;
    gap: 14px;
  }
  .brand-dot {
    flex: none;
    width: 50px;
    height: 50px;
    border-radius: 50%;
    background: var(--brand-light);
  }
  .brand-name {
    font-family: "Montserrat", Arial, sans-serif;
    font-weight: 600;
    font-size: 31px;
    letter-spacing: 1px;
    white-space: nowrap;
    color: var(--brand-light);
    text-transform: uppercase;
  }
  .contact {
    list-style: none;
    color: var(--brand-light);
    font-size: 12px;
    font-weight: 700;
    text-align: right;
    white-space: nowrap;
  }
  .contact li {
    display: flex;
    justify-content: flex-end;
    align-items: center;
    gap: 8px;
    line-height: 19px;
  }
  .contact .gap { margin-top: 16px; }
  .contact .no-icon { padding-right: 22px; }
  .contact svg { width: 14px; height: 14px; flex: none; }
  .letter-body {
    position: relative;
    padding: 42px 46px 0 46px;
  }
  .recipient {
    font-style: normal;
    font-weight: 700;
    font-size: 14.5px;
    line-height: 26px;
    margin-bottom: 12px;
  }
  .letter-body p.copy {
    font-size: 13.8px;
    line-height: 18.4px;
    margin-bottom: 18px;
    width: 640px;
  }
  .sign-off {
    font-weight: 700;
    font-size: 12.5px;
    margin-top: 20px;
  }
  .signature {
    width: 124px;
    height: 54px;
    margin: 10px 0 22px;
    background: var(--signature);
  }
  .signer {
    font-weight: 700;
    font-size: 12.5px;
  }
</style>
</head>
<body>
  <main class="letterhead">
    <div class="watermark-circle"></div>

    <header class="header-band">
      <div class="brand">
        <span class="brand-dot"></span>
        <span class="brand-name">Quillridge Acres</span>
      </div>
      <ul class="contact">
        <li class="no-icon">415 Bramwell Avenue #600</li>
        <li>Dallas, TX 75219
          <svg viewBox="0 0 14 14"><circle cx="7" cy="7" r="7" fill="#fff"/><path d="M7 3a2.6 2.6 0 0 0-2.6 2.6C4.4 7.8 7 11 7 11s2.6-3.2 2.6-5.4A2.6 2.6 0 0 0 7 3zm0 3.6a1 1 0 1 1 0-2 1 1 0 0 1 0 2z" fill="#4a5d23"/></svg>
        </li>
        <li class="gap">866-402-ACRE
          <svg viewBox="0 0 14 14"><circle cx="7" cy="7" r="7" fill="#fff"/><path d="M4.6 3.6l1.3-.2.7 1.8-.8.7a5 5 0 0 0 2.3 2.3l.7-.8 1.8.7-.2 1.3c-3.3.3-6.1-2.5-5.8-5.8z" fill="#4a5d23"/></svg>
        </li>
        <li>info@quillridgeacres.example
          <svg viewBox="0 0 14 14"><circle cx="7" cy="7" r="7" fill="#fff"/><rect x="3.6" y="4.6" width="6.8" height="4.8" fill="none" stroke="#4a5d23" stroke-width="1"/><path d="M3.6 4.6 7 7.2l3.4-2.6" fill="none" stroke="#4a5d23" stroke-width="1"/></svg>
        </li>
        <li>www.quillridgeacres.example
          <svg viewBox="0 0 14 14"><circle cx="7" cy="7" r="7" fill="#fff"/><circle cx="7" cy="7" r="3.6" fill="none" stroke="#4a5d23" stroke-width="1"/><path d="M3.4 7h7.2M7 3.4c-1.8 2-1.8 5.2 0 7.2M7 3.4c1.8 2 1.8 5.2 0 7.2" fill="none" stroke="#4a5d23" stroke-width=".8"/></svg>
        </li>
      </ul>
    </header>

    <section class="letter-body">
      <address class="recipient">
        To<br>
        Mr. Dorian Pellham<br>
        4870 Larkspur Lane,<br>
        Plano, TX
      </address>

      <p class="copy">Lorem ipsum dolor sit amet, consectetur adipiscing elit. Donec eget nisi eget tortor iaculis tristique. Aliquam tincidunt posuere tortor hendrerit elementum. Nunc laoreet lorem a sem auctor fringilla. Pellentesque dignissim accumsan lobortis. Sed pharetra erat vitae dui imperdiet quis commodo orci dapibus. Cum sociis natoque penatibus et magnis dis parturient montes, nascetur ridiculus mus. Fusce at nunc libero. Nam metus lorem, rhoncus ac mattis ornare, blandit vel risus.Vestibulum ante ipsum primis in faucibus orci luctus et ultrices posuere cubilia Curae; Ut sit amet augue eget purus facilisis suscipit. Sed vitae risus nibh. Vivamus at sollicitudin ipsum. Vestibulum consectetur dictum egestas. Nam eu tortor non mauris condimentum rutrum eu at urna. Vivamus quis odio et velit aliquet adipiscing quis quis diam. Quisque facilisis molestie neque, in consequat tortor viverra eu.</p>

      <p class="copy">Vestibulum ante ipsum primis in faucibus orci luctus et ultrices posuere cubilia Curae; Ut sit amet augue eget purus facilisis suscipit. Sed vitae risus nibh. Vivamus at sollicitudin ipsum. Vestibulum consectetur dictum egestas. Nam eu tortor non mauris condimentum rutrum eu at urna. Vivamus quis odio et velit aliquet adipiscing quis quis diam. Quisque facilisis molestie neque, in consequat tortor viverra eu.</p>

      <p class="copy">Etiam tincidunt aliquam porta. Phasellus ut nisi nibh. Pellentesque non nulla nisi. Sed interdum porta leo ut interdum. Integer molestie, libero quis pellentesque gravida, sapien sem varius est, vel sagittis libero sapien id nulla. Vivamus aliquam nulla vitae mi sodales sit amet semper nulla pulvinar. Nulla congue sagittis auctor. Pellentesque sollicitudin mollis libero.</p>

      <p class="copy">rutrum eu at urna. Vivamus quis odio et velit aliquet adipiscing quis quis diam. Quisque facilisis molestie neque, in consequat tortor viverra eu.</p>

      <p class="sign-off">Yours faithfully,</p>
      <div class="signature" role="img" aria-label="Handwritten signature of the sender"></div>
      <p class="signer">Evan Thomas Reed</p>
    </section>
  </main>
</body>
</html>
```